Baby Shower Invitation for Vectored Image Provided

Caroline & Desmond's Baby Shower - Black/White/Gold Colors preferred
Please use the vectored portrait image attached. I'd like us on the lower right side of the invitation.
Can be horizontal or vertical layout.
The second image attached has the information needed for you to complete.
I don't want that style copied, it is just an example.

```html
<!DOCTYPE html>
<html lang="en">
<head>
<meta charset="utf-8">
<title>Baby Shower Invitation – Caroline Hartwell</title>
<link rel="stylesheet" href="https://fonts.googleapis.com/css2?family=Pacifico&family=Special+Elite&display=block">
<style>
  :root {
    --black-deep: #0b0b0c;
    --black: #17171a;
    --charcoal: #26262b;
    --white: #ffffff;
    --ink: #2a1e08;
    --gold-dark: #9a6a10;
    --gold: #d4a52a;
    --gold-light: #f6e7a8;
    --gold-rule: rgba(226, 190, 96, 0.9);
    --portrait-dark: #1c1c22;
    --portrait-mid: #6e5446;
  }
  * { margin: 0; padding: 0; box-sizing: border-box; }
  html, body { width: 851px; height: 1200px; overflow: hidden; }
  body { background: var(--black-deep); }

  .invitation {
    position: relative;
    width: 851px;
    height: 1200px;
    overflow: hidden;
    color: var(--white);
    background:
      radial-gradient(ellipse at 30% 20%, var(--charcoal) 0%, transparent 55%),
      radial-gradient(ellipse at 80% 70%, var(--charcoal) 0%, transparent 50%),
      linear-gradient(160deg, var(--black) 0%, var(--black-deep) 100%);
    font-family: "Special Elite", "Courier Prime", "Courier New", monospace;
  }

  .frame {
    position: absolute;
    left: 45px; top: 60px;
    width: 735px; height: 1045px;
    border: 2px dotted var(--gold-rule);
  }

  .centered { position: absolute; left: 0; width: 825px; text-align: center; }

  .headline {
    top: 88px;
    font-family: "Pacifico", cursive;
    font-weight: 400;
    font-size: 132px;
    line-height: 1;
    white-space: nowrap;
  }
  .headline .baby-art {
    display: inline-block;
    width: 86px; height: 110px;
    margin: 0 2px;
    vertical-align: -4px;
    border-radius: 50% / 52%;
    background: radial-gradient(circle at 45% 40%, #ffffff 0%, #f3f0e6 75%, #e2d2a0 100%);
  }

  .tagline {
    top: 312px;
    font-size: 38px;
    letter-spacing: 6px;
    line-height: 52px;
  }

  .invite-line {
    top: 428px;
    font-size: 30px;
    line-height: 38px;
  }

  .honoree {
    top: 515px;
    font-family: "Pacifico", cursive;
    font-weight: 400;
    font-size: 46px;
    line-height: 1.3;
  }

  .rule { position: absolute; border-color: var(--gold-rule); border-style: dotted; border-width: 0; }
  .rule-top { left: 168px; top: 606px; width: 488px; border-top-width: 2px; }
  .rule-bottom { left: 168px; top: 768px; width: 488px; border-top-width: 2px; }
  .rule-divider { left: 434px; top: 606px; height: 162px; border-left-width: 2px; }
  .rule-time { left: 434px; top: 654px; width: 222px; border-top-width: 2px; }

  .event-date {
    position: absolute;
    left: 168px; top: 628px;
    width: 262px;
    text-align: center;
    line-height: 1;
  }
  .event-date .weekday { font-size: 40px; display: block; }
  .event-date .day { font-size: 52px; display: block; margin-top: 14px; }
  .event-date sup { font-size: 26px; line-height: 0; vertical-align: 20px; }

  .event-time {
    position: absolute;
    left: 452px; top: 616px;
    font-size: 25px;
  }
  .event-venue {
    position: absolute;
    left: 452px; top: 664px;
    font-size: 25px;
    line-height: 32px;
  }

  .rsvp-band {
    position: absolute;
    left: 0; top: 808px;
    width: 825px; height: 145px;
    background: linear-gradient(90deg, var(--gold-dark) 0%, var(--gold) 45%, var(--gold-light) 100%);
  }
  .rsvp {
    position: absolute;
    left: 90px; top: 824px;
    width: 490px;
    text-align: center;
    color: var(--ink);
    font-size: 30px;
    line-height: 38px;
  }

  .registry {
    position: absolute;
    left: 90px; top: 1020px;
    width: 490px;
    text-align: center;
    font-family: "Pacifico", cursive;
    font-weight: 400;
    font-size: 26px;
    line-height: 46px;
  }

  .portrait {
    position: absolute;
    left: 530px; top: 810px;
    width: 238px; height: 312px;
    border-radius: 105px 105px 0 0;
    background: linear-gradient(180deg, var(--portrait-mid) 0%, var(--portrait-dark) 45%, var(--portrait-dark) 100%);
  }
</style>
</head>
<body>
<main class="invitation">
  <div class="frame"></div>

  <h1 class="centered headline">Oh B<span class="baby-art" role="img" aria-label="Illustration of a swaddled baby forming the letter o"></span>y !</h1>

  <p class="centered tagline">A LITTLE MAN<br>IS ON THE WAY!</p>

  <p class="centered invite-line">Please join us for a<br>Baby Shower honoring</p>

  <h2 class="centered honoree">Caroline Hartwell</h2>

  <div class="rule rule-top"></div>
  <div class="rule rule-bottom"></div>
  <div class="rule rule-divider"></div>
  <div class="rule rule-time"></div>

  <p class="event-date">
    <span class="weekday">Saturday</span>
    <span class="day">1<sup>st</sup> Sept</span>
  </p>
  <p class="event-time">11:30am-2:30pm</p>
  <p class="event-venue">The Maplewood<br>1480 Bramble St.<br>Raleigh, NC</p>

  <div class="rsvp-band"></div>
  <p class="rsvp">RSVP to Desmond at<br>919-555-0148<br>by August 20th</p>

  <p class="registry">Caroline is registered at<br>Cradle &amp; Co</p>

  <div class="portrait" role="img" aria-label="Vector portrait of the expecting couple, standing together in black outfits"></div>
</main>
</body>
</html>
```